GHollis Busisness Card

I am an aerospace consultant and at this time only need business cards.

Industry/Entity Type

Business

Contact Information for Business Card

Hollis Partners,LLC
Gerald T. Hollis

348 Birch Hollow Road
Madison AL 35762

256-555-0148 (cell)
256-555-0173 (fax)

geraldhollis@mailbrook.net

```html
<!DOCTYPE html>
<html lang="en">
<head>
<meta charset="utf-8">
<title>Gerald Hollis – Business Card</title>
<link href="https://fonts.googleapis.com/css2?family=Arimo:wght@400;700&display=swap" rel="stylesheet">
<style>
  :root {
    --backdrop: #1c1d1f;
    --card: #4a4b4e;
    --ink: #ececea;
    --accent: #8dc63f;
  }
  * { margin: 0; padding: 0; box-sizing: border-box; }
  html, body {
    width: 1200px;
    height: 1000px;
    overflow: hidden;
    background: var(--backdrop);
    font-family: "Arimo", Arial, sans-serif;
  }
  .business-card {
    position: absolute;
    left: 150px;
    top: 243px;
    width: 900px;
    height: 514px;
    background: var(--card);
    color: var(--ink);
  }
  .brand {
    position: absolute;
    left: 70px;
    top: 218px;
    display: flex;
    align-items: center;
    gap: 14px;
  }
  .brand-dot {
    width: 26px;
    height: 26px;
    border-radius: 50%;
    background: var(--accent);
  }
  .brand-name {
    font-size: 36px;
    font-weight: 700;
    color: var(--ink);
  }
  .details {
    position: absolute;
    left: 500px;
    top: 64px;
  }
  .person-name {
    font-size: 40px;
    font-weight: 700;
    letter-spacing: 0.5px;
  }
  .person-title {
    margin-top: 10px;
    font-size: 19px;
    color: var(--accent);
  }
  .contact {
    margin-top: 24px;
    list-style: none;
    font-size: 23px;
    line-height: 36px;
  }
  .contact-label {
    display: inline-block;
    width: 42px;
    color: var(--accent);
  }
  .address {
    margin-top: 24px;
    margin-left: -20px;
    font-style: normal;
    font-size: 23px;
    line-height: 34px;
  }
</style>
</head>
<body>
  <section class="business-card">
    <div class="brand">
      <span class="brand-dot"></span>
      <span class="brand-name">Hollis Partners</span>
    </div>
    <div class="details">
      <h1 class="person-name">Gerald Hollis</h1>
      <p class="person-title">Aerospace Consultant</p>
      <ul class="contact">
        <li><span class="contact-label">T:</span>(256) 555-0148</li>
        <li><span class="contact-label">F:</span>(256) 555-0173</li>
        <li><span class="contact-label">E:</span>geraldhollis@mailbrook.net</li>
      </ul>
      <address class="address">
        Hollis Partners,<br>
        LLC Gerald T. Hollis<br>
        348 Birch Hollow Road<br>
        Madison AL 35762
      </address>
    </div>
  </section>
</body>
</html>
```